Computer consultant business card

Brimlo Software is a newly started computer consulting company. It's a small one-man company that provides mostly Velunix applications but also websites in collaboration with designers. I'm running this company on the side of full time university studies.

I want the final design to be clean and memorable. Be creative! :)

Some inspiration:
http://www.tavelpix.net/design/73519
http://www.tavelpix.net/design/2739566/business-card-design-by-quillbop
http://www.tavelpix.net/design/804613/business-card-design-by-lorvena-brukwaldsen

See attachment for my company logo.
Updates

I would like to thank everyone for submitting! I'll need a couple of days to review and ultimately select a design.

Target Market(s)

Non-technical entrepreneurs and small companies.

Industry/Entity Type

University

Requirements
Must have
• My company logo.
In any way, both colors from my logo.
First- and last name, e-mail and phone number.
Double-sided design.
Nice to have
• Something creative with the symbol in my logo

```html
<!DOCTYPE html>
<html lang="en">
<head>
<meta charset="utf-8">
<title>Brimlo Software – Business Card</title>
<link rel="stylesheet" href="https://fonts.googleapis.com/css2?family=Open+Sans:wght@300;400;700&display=swap">
<style>
  :root {
    --page-bg: #e4e6ea;
    --blue-deep: #1f4fae;
    --blue-mid: #0f8fd0;
    --blue-bright: #2bb7e6;
    --blue-light: #7fd3f2;
    --ink-grey: #555a60;
    --ink-dark: #2a2d31;
    --phone-blue: #2c6cc4;
    --card-white: #ffffff;
    --swirl-grey: #f1f2f4;
  }
  html, body {
    margin: 0;
    padding: 0;
    width: 1200px;
    height: 1000px;
    overflow: hidden;
    background: var(--page-bg);
    font-family: "Open Sans", Arial, sans-serif;
  }
  .canvas {
    position: relative;
    width: 1200px;
    height: 1000px;
  }
  .card {
    position: absolute;
    left: 250px;
    width: 700px;
    height: 400px;
    overflow: hidden;
    box-shadow: 0 10px 30px rgba(0,0,0,0.18);
  }
  .card svg.card-bg {
    position: absolute;
    inset: 0;
  }

  /* Front */
  .card-front { top: 60px; }
  .front-brand {
    position: absolute;
    inset: 0;
    display: flex;
    align-items: center;
    justify-content: center;
    gap: 22px;
  }
  .brand-dot {
    width: 54px;
    height: 54px;
    border-radius: 50%;
    background: var(--card-white);
  }
  .brand-name {
    color: var(--card-white);
    font-weight: 700;
    font-size: 92px;
    letter-spacing: 2px;
    line-height: 1;
  }

  /* Back */
  .card-back { top: 540px; background: var(--card-white); }
  .back-brand {
    position: absolute;
    top: 40px;
    left: 48px;
    display: flex;
    align-items: center;
    gap: 12px;
  }
  .back-brand .brand-dot {
    width: 26px;
    height: 26px;
    background: var(--blue-mid);
  }
  .back-brand .brand-name {
    color: var(--blue-mid);
    font-size: 38px;
    letter-spacing: 1px;
  }
  .person {
    position: absolute;
    left: 48px;
    top: 150px;
  }
  .person-name {
    margin: 0;
    font-weight: 300;
    font-size: 54px;
    color: var(--ink-grey);
    line-height: 1.05;
  }
  .person-title {
    margin: 4px 0 0;
    font-size: 19px;
    color: var(--ink-grey);
    letter-spacing: 0.5px;
  }
  .contact {
    position: absolute;
    left: 48px;
    bottom: 40px;
    margin: 0;
    font-weight: 700;
    font-size: 20px;
    line-height: 1.45;
  }
  .contact-email { color: var(--ink-dark); display: block; }
  .contact-phone { color: var(--phone-blue); display: block; }
</style>
</head>
<body>
<main class="canvas">

  <section class="card card-front" aria-label="Card front">
    <svg class="card-bg" width="700" height="400" viewBox="0 0 700 400" aria-hidden="true">
      <defs>
        <linearGradient id="frontGradient" x1="0" y1="1" x2="1" y2="0">
          <stop offset="0" stop-color="#1f4fae"/>
          <stop offset="0.45" stop-color="#0f9ad6"/>
          <stop offset="0.7" stop-color="#3fc0ea"/>
          <stop offset="1" stop-color="#1a7fcc"/>
        </linearGradient>
      </defs>
      <rect width="700" height="400" fill="url(#frontGradient)"/>
      <path d="M0 120 C 140 140, 230 230, 210 400 L 0 400 Z" fill="#1c4aa6" opacity="0.45"/>
      <path d="M0 220 C 90 230, 160 300, 150 400 L 0 400 Z" fill="#173f94" opacity="0.35"/>
      <path d="M700 60 C 560 40, 470 100, 480 0 L 700 0 Z" fill="#1f5fb8" opacity="0.35"/>
      <path d="M700 170 C 600 150, 520 110, 560 0 L 700 0 Z" fill="#2456b0" opacity="0.3"/>
    </svg>
    <div class="front-brand">
      <span class="brand-dot"></span>
      <span class="brand-name">brimlo</span>
    </div>
  </section>

  <section class="card card-back" aria-label="Card back">
    <svg class="card-bg" width="700" height="400" viewBox="0 0 700 400" aria-hidden="true">
      <rect width="700" height="400" fill="#ffffff"/>
      <path d="M700 0 C 560 80, 500 220, 560 400 L 700 400 Z" fill="#f1f2f4"/>
      <path d="M330 400 C 360 300, 430 250, 520 240 C 470 300, 450 350, 460 400 Z" fill="#f5f6f7"/>
    </svg>
    <div class="back-brand">
      <span class="brand-dot"></span>
      <span class="brand-name">brimlo</span>
    </div>
    <div class="person">
      <h1 class="person-name">Maren Tolsby</h1>
      <p class="person-title">Professional developer</p>
    </div>
    <p class="contact">
      <span class="contact-email">maren@brimlo.net</span>
      <span class="contact-phone">(555) 318-2047</span>
    </p>
  </section>

</main>
</body>
</html>
```